We are a music company that specializes in Music Mixing and Mastering. We also do vocal recording and create instrumentals for various artists. Our website is 738kv.com

Target Market(s)

Musicians, Record labels, rappers, and singers

Industry/Entity Type

Artists

Contact Information for Business Card

738KV
Industry Standard Mixing & Mastering
(555) 214-3907
sales@738kv.com
738kv.com

Requirements
Must have
• contact info and twitter (@738KV)

```html
<!DOCTYPE html>
<html lang="en">
<head>
<meta charset="utf-8">
<title>738KV Business Card</title>
<link rel="stylesheet" href="https://fonts.googleapis.com/css2?family=Quicksand:wght@400;500;700&display=swap">
<style>
  :root {
    --page: #2a2c31;
    --card-white: #f4f4f2;
    --ink: #1b1b1b;
    --band: #1f1f1f;
    --card-black: #0c0c0c;
    --accent-red: #c8202a;
    --paper-text: #ffffff;
  }
  * { margin: 0; padding: 0; box-sizing: border-box; }
  html, body {
    width: 1200px; height: 900px; overflow: hidden;
    background: var(--page);
    font-family: "Quicksand", sans-serif;
  }
  .sheet {
    position: relative; width: 1200px; height: 900px;
    display: flex; flex-direction: column; align-items: center;
    justify-content: center; gap: 40px;
  }
  .card {
    position: relative; width: 700px; height: 400px;
    box-shadow: 0 12px 30px rgba(0,0,0,.45);
    overflow: hidden;
  }

  /* Front */
  .card-front { background: var(--card-white); color: var(--ink); }
  .front-brand {
    position: absolute; left: 60px; top: 40px;
    font-size: 150px; font-weight: 700; line-height: 1; letter-spacing: -2px;
    color: var(--ink);
  }
  .front-tagline {
    position: absolute; left: 62px; top: 218px;
    font-size: 33px; font-weight: 500; color: var(--ink);
  }
  .front-rule {
    position: absolute; left: 0; right: 0; top: 282px;
    height: 3px; background: var(--ink);
  }
  .contact-band {
    position: absolute; left: 0; right: 0; bottom: 0; height: 100px;
    background: var(--band); color: var(--paper-text);
    display: flex; align-items: center; justify-content: center; gap: 14px;
    font-size: 17px; font-weight: 400;
  }
  .contact-band .label { font-weight: 700; }
  .contact-band .divider { opacity: .8; }

  /* Back */
  .card-back { background: var(--card-black); color: var(--accent-red); }
  .back-brand {
    position: absolute; left: 60px; top: 50px;
    font-size: 150px; font-weight: 700; line-height: 1; letter-spacing: -2px;
    color: var(--accent-red);
  }
  .back-tagline {
    position: absolute; left: 62px; top: 228px;
    font-size: 33px; font-weight: 500; color: var(--accent-red);
  }
  .social-handle {
    position: absolute; left: 62px; bottom: 40px;
    display: flex; align-items: center; gap: 12px;
    color: var(--paper-text); font-size: 22px; font-weight: 700;
  }
  .social-square {
    width: 28px; height: 28px; border-radius: 5px; background: #3b8fd4;
  }
</style>
</head>
<body>
  <main class="sheet">
    <section class="card card-front" aria-label="Business card front">
      <div class="front-brand">738KV</div>
      <div class="front-tagline">Industry Standard Mixing &amp; Mastering</div>
      <div class="front-rule"></div>
      <div class="contact-band">
        <span><span class="label">Phone:</span> (555) 214-3907</span>
        <span class="divider">|</span>
        <span><span class="label">Email:</span> sales@738kv.com</span>
        <span class="divider">|</span>
        <span><span class="label">Web:</span> www.738kv.com</span>
      </div>
    </section>

    <section class="card card-back" aria-label="Business card back">
      <div class="back-brand">738KV</div>
      <div class="back-tagline">Industry Standard Mixing &amp; Mastering</div>
      <div class="social-handle">
        <span class="social-square"></span>
        <span>738KV</span>
      </div>
    </section>
  </main>
</body>
</html>
```